Walk Bright through the Seasons: 52 Weeks to a Year of Courage and Calm

This is a non-fiction, self-help book. The first edition was published a decade ago, and it needs a new design. Nothing too literal (no actual hearts on the cover) but something inspirational or perhaps something quite plain. The current cover is below for reference, but I DO NOT want something similar to that. It is outdated.

The cover must include:

1. Title: Walk Bright through the Seasons
2. Subtitle: 52 Weeks to a Year of Courage and Calm
3. Author Name: Tobin Wells

It should also have plenty of "white space" in other words the fonts shouldnt be so big that they take up the whole cover.

Dimensions: 9" x 6.25"

Target Market(s)

adults interested in personal development

Font styles to use
Serif
Script

Colors

Designer to choose colors to be used in the design.

Requirements
Must have
• Classic look and feel. The current design is too busy. I have included examples of the style I like below. I'm open to a singular graphic/photo but nothing more than that. Probably plain text is best.
• Please look at the samples I have included of best-selling books in the genre that I like. The cover should be modeled after these.

```html
<!DOCTYPE html>
<html lang="en">
<head>
<meta charset="utf-8">
<title>Walk Bright through the Seasons — Tobin Wells</title>
<link rel="stylesheet" href="https://fonts.googleapis.com/css2?family=Abril+Fatface&family=Playfair+Display:ital,wght@1,700&family=Lobster&family=Prata&display=swap">
<style>
  :root {
    --paper: #ffffff;
    --ink: #111111;
    --royal-blue: #175da9;
    --mist-blue: #8badd4;
    --sun-yellow: #f6bf1b;
    --gradient-start: #0093d3;
    --gradient-mid: #7aa978;
    --gradient-end: #fcc419;
  }
  html, body {
    margin: 0;
    padding: 0;
    width: 933px;
    height: 1200px;
    overflow: hidden;
    background: var(--paper);
  }
  .book-cover {
    display: block;
    width: 933px;
    height: 1200px;
  }
  .title-main {
    font-family: "Abril Fatface", serif;
    font-size: 160px;
    fill: var(--royal-blue);
  }
  .title-connector {
    font-family: "Playfair Display", serif;
    font-style: italic;
    font-weight: 700;
    font-size: 66px;
    fill: var(--mist-blue);
  }
  .title-script {
    font-family: "Lobster", cursive;
    font-size: 270px;
  }
  .subtitle {
    font-family: "Prata", serif;
  }
  .subtitle-lead { font-size: 60px; fill: var(--sun-yellow); }
  .subtitle-join { font-size: 40px; fill: var(--ink); }
  .subtitle-tail { font-size: 42px; fill: var(--royal-blue); }
  .author-name {
    font-family: "Abril Fatface", serif;
    font-size: 60px;
    fill: var(--ink);
  }
</style>
</head>
<body>
<svg class="book-cover" viewBox="0 0 933 1200" xmlns="http://www.w3.org/2000/svg" role="img" aria-label="Walk Bright through the Seasons: 52 Weeks to a Year of Courage and Calm, by Tobin Wells">
  <defs>
    <linearGradient id="script-gradient" x1="68" y1="0" x2="856" y2="0" gradientUnits="userSpaceOnUse">
      <stop offset="0" stop-color="var(--gradient-start)"/>
      <stop offset="0.5" stop-color="var(--gradient-mid)"/>
      <stop offset="1" stop-color="var(--gradient-end)"/>
    </linearGradient>
  </defs>
  <rect width="933" height="1200" fill="var(--paper)"/>

  <g class="title">
    <text class="title-main" x="118" y="255">Walk</text>
    <text class="title-main" x="118" y="428">Bright</text>
    <text class="title-connector" x="120" y="535">through the</text>
    <text class="title-script" x="68" y="789" textLength="788" lengthAdjust="spacingAndGlyphs" fill="url(#script-gradient)">Seasons</text>
  </g>

  <g class="subtitle">
    <text x="120" y="878"><tspan class="subtitle-lead">52 Weeks</tspan><tspan class="subtitle-join" dx="14">to a</tspan></text>
    <text class="subtitle-tail" x="120" y="933">Year of Courage and Calm</text>
  </g>

  <text class="author-name" x="466" y="1124" text-anchor="middle">Tobin Wells</text>
</svg>
</body>
</html>
```